sydney wedding photography business needs a business card design

we need a business card design for a sydney based wedding photography and videography business. our business name is :golden hour photography and video. our target clients are 24-35 yrs female. our style is candid, organic, natural, dynamic. we are a team of young photographers and videographers, and help brides to create memories that they will cherish for the rest of their lives. the logo will be provided. we want an elegant design that reflects our style, and also want to give a great impression to our clients that we are one of the best studios in sydney and our brand means quality and premium service.

Target Market(s)

bride to be, 24-35 years old, living in sydney and surrunding areas

Industry/Entity Type

Wedding Photography

Contact Information for Business Card

address: 57 marrow lane, bexton nsw 2041
mobile: 0431872056
phone: (02) 9361 2748
info@goldenhourstudio.net.au
www.goldenhourstudio.net.au
facebook:goldenhourbridals
instagram:goldenhourbridals

Font styles to use
Serif
Sans Serif

Requirements
Nice to have
• maybe add my slogan"memories beyond eternity" if the layout looks good
Should not have
• no black color, not good idea for wedding biz card

```html
<!DOCTYPE html>
<html lang="en">
<head>
<meta charset="utf-8">
<title>Golden Hour Photography – Business Card</title>
<link rel="stylesheet" href="https://fonts.googleapis.com/css2?family=Damion&family=Open+Sans:wght@400;600&display=swap">
<style>
  :root {
    --backdrop: #ece7df;
    --card: #ffffff;
    --gold: #c99a28;
    --gold-light: #f2c417;
    --ink: #2b2b2b;
    --pattern: #fbf8ee;
  }
  * { margin: 0; padding: 0; box-sizing: border-box; }
  html, body {
    width: 1200px; height: 1000px; overflow: hidden;
    background: var(--backdrop);
  }
  .canvas { position: relative; width: 1200px; height: 1000px; }
  .card {
    position: absolute; left: 265px; width: 666px; height: 397px;
    background: var(--card); border-radius: 24px; overflow: hidden;
    box-shadow: 0 4px 14px rgba(60, 40, 20, 0.18);
  }
  .card-front { top: 73px; }
  .card-back { top: 533px; }

  .holder-name {
    position: absolute; left: 33px; top: 62px;
    font-family: "Damion", cursive; font-size: 36px; color: var(--gold);
    line-height: 1;
  }
  .holder-role {
    position: absolute; left: 33px; top: 106px;
    font-family: "Open Sans", sans-serif; font-size: 16px; color: var(--ink);
  }
  .contact-list {
    position: absolute; left: 33px; top: 181px; list-style: none;
    font-family: "Open Sans", sans-serif; font-size: 16px; color: var(--ink);
  }
  .contact-list li { display: flex; align-items: center; height: 24px; }
  .contact-list li.social { margin-top: 3px; }
  .contact-icon { width: 14px; height: 14px; margin-right: 8px; flex: none; }
  .social-mark {
    width: 11px; height: 11px; background: var(--gold); margin-right: 8px; flex: none;
  }
  .address {
    position: absolute; left: 33px; top: 320px;
    font-family: "Open Sans", sans-serif; font-size: 16px; color: var(--ink);
  }
  .front-brand {
    position: absolute; left: 356px; top: 160px; width: 280px;
    display: flex; align-items: center; gap: 12px;
  }
  .brand-dot {
    width: 22px; height: 22px; border-radius: 50%; background: var(--gold); flex: none;
  }
  .front-brand-name {
    font-family: "Open Sans", sans-serif; font-weight: 600; font-size: 36px;
    color: var(--gold); white-space: nowrap;
  }

  .back-field {
    position: absolute; inset: 0; background: var(--pattern);
  }
  .back-brand {
    position: absolute; left: 0; right: 0; top: 172px; text-align: center;
    font-family: "Open Sans", sans-serif; font-weight: 600; font-size: 42px;
    color: var(--gold);
  }
</style>
</head>
<body>
<main class="canvas">
  <section class="card card-front" aria-label="Business card front">
    <p class="holder-name">Daniel R. Whitford</p>
    <p class="holder-role">Wedding Photographer</p>
    <ul class="contact-list">
      <li>
        <svg class="contact-icon" viewBox="0 0 14 14" aria-hidden="true">
          <rect x="3.5" y="0.5" width="7" height="13" rx="1.5" fill="none" stroke="#c99a28" stroke-width="1.3"/>
          <rect x="5.5" y="10.5" width="3" height="1.2" fill="#c99a28"/>
        </svg>0431872056
      </li>
      <li>
        <svg class="contact-icon" viewBox="0 0 14 14" aria-hidden="true">
          <path d="M1 5 Q7 1 13 5 L12 7 L9.5 6 L9.5 4.8 Q7 4 4.5 4.8 L4.5 6 L2 7 Z" fill="#c99a28"/>
          <rect x="3" y="7.5" width="8" height="5" rx="1" fill="#c99a28"/>
        </svg>(02) 9361 2748
      </li>
      <li>
        <svg class="contact-icon" viewBox="0 0 14 14" aria-hidden="true">
          <rect x="0.5" y="3" width="13" height="8.5" fill="#c99a28"/>
          <path d="M0.5 3 L7 8 L13.5 3" fill="none" stroke="#fff" stroke-width="1"/>
        </svg>info@goldenhourstudio.net.au
      </li>
      <li>
        <svg class="contact-icon" viewBox="0 0 14 14" aria-hidden="true">
          <circle cx="7" cy="7" r="6" fill="none" stroke="#c99a28" stroke-width="1.3"/>
          <ellipse cx="7" cy="7" rx="2.6" ry="6" fill="none" stroke="#c99a28" stroke-width="1"/>
          <line x1="1" y1="7" x2="13" y2="7" stroke="#c99a28" stroke-width="1"/>
        </svg>www.goldenhourstudio.net.au
      </li>
      <li class="social">
        <span class="social-mark" aria-hidden="true"></span>goldenhourbridals
      </li>
    </ul>
    <p class="address">57 Marrow Lane, Bexton NSW 2041</p>
    <div class="front-brand">
      <span class="brand-dot" aria-hidden="true"></span>
      <span class="front-brand-name">Golden Hour</span>
    </div>
  </section>

  <section class="card card-back" aria-label="Business card back">
    <div class="back-field" role="img" aria-label="Faint repeating background pattern in pale cream"></div>
    <p class="back-brand">Golden Hour Photography</p>
  </section>
</main>
</body>
</html>
```